Website Online Research Solutions

We are a small European high-tech online research company.
With our own state of the art software we run online panels and are conducting reseach for companies. Partly research via our own panel and partly via panels we maintain for our customers.
Our current website is old and outdatet: www.pravelo.nl.
We are in the process to change the content of the site. We want a modern, european and businesslike design for our new website.
Our logo has to stay the same (left uppersite of our website and attached) but can be changed a little to adapt it to the new design of the website. The colors of the site are up to you.
Target Market(s)
Marketeers and researchers of large and middle size companies in all kind of fields.
Industry/Entity Type
Online
Look and feel
Each slider illustrates characteristics of the customer's brand and the style your logo design should communicate.

```html
<!DOCTYPE html>
<html lang="nl">
<head>
<meta charset="utf-8">
<title>Pravelo – Online Research Solutions</title>
<link href="https://fonts.googleapis.com/css2?family=Arimo:wght@400;700&display=swap" rel="stylesheet">
<style>
:root{
  --navy-deep:#0d2a5a;
  --navy:#1a4c8c;
  --navy-light:#2a62a8;
  --band:#1b2a52;
  --band-dark:#14213f;
  --ink:#111;
  --heading:#163a6e;
  --muted:#555;
  --accent:#2a8fe0;
  --footer:#7a7a7a;
  --footer-text:#d6d6d6;
  --white:#fff;
}
*{margin:0;padding:0;box-sizing:border-box}
html,body{width:1200px;height:1050px;overflow:hidden;background:#fff}
body{font-family:"Arimo",Helvetica,Arial,sans-serif;color:var(--ink);position:relative}
.abs{position:absolute}

/* Header */
.hero{left:0;top:0;width:1200px;height:408px;
  background:radial-gradient(ellipse at 70% 45%,var(--navy-light) 0%,var(--navy) 45%,var(--navy-deep) 100%)}
.utility{right:115px;top:23px;font-size:11px;color:#cfe0f5}
.utility span{margin:0 10px}
.brand{left:135px;top:20px;width:190px;height:190px;display:flex;align-items:center;justify-content:center;gap:10px}
.brand-mark{width:22px;height:22px;border-radius:50%;background:#c9ced6}
.brand-name{font-size:34px;font-weight:700;color:#e6e9ee}
.nav{top:96px;left:0;width:1200px;height:26px}
.nav a{position:absolute;top:0;line-height:26px;font-size:14px;font-weight:700;color:var(--white);text-decoration:none;transform:translateX(-50%)}
.nav a.active{background:#163e74;border-radius:13px;padding:0 28px;box-shadow:inset 0 1px 3px rgba(0,0,0,.35)}
.hero-title{left:196px;top:236px;font-size:30px;font-weight:700;color:var(--white);text-shadow:0 1px 2px rgba(0,0,0,.4)}
.hero-text{left:196px;top:274px;width:420px;font-size:17px;line-height:29px;color:#e3ecf7}
.hero-photo{left:600px;top:124px;width:465px;height:284px;
  background:radial-gradient(ellipse at 50% 40%,#d9c2ae 0%,#8c8f9c 40%,rgba(40,60,100,0.2) 75%,rgba(26,76,140,0) 100%);
  border-radius:40% 40% 0 0}

/* Sub band */
.band{left:0;top:408px;width:1200px;height:70px;background:linear-gradient(var(--band),var(--band-dark))}
.teaser{top:424px;display:flex;gap:10px;align-items:flex-start}
.teaser svg{margin-top:4px}
.teaser p{font-size:16px;font-weight:700;color:var(--white);line-height:20px}
.teaser b{color:var(--accent);font-size:13px}

/* Content */
.welcome{left:166px;top:494px;font-size:28px;font-weight:700;color:var(--heading)}
.lead{left:166px;top:532px;width:490px;font-size:13px;font-weight:700;line-height:18px;color:var(--muted);letter-spacing:-.2px}
.body-copy{left:166px;top:574px;width:500px;font-size:11px;line-height:17px;color:var(--ink);letter-spacing:-.15px}
.body-copy p{margin-bottom:7px}
.site{top:734px;width:138px}
.site .shot{width:138px;height:95px;border:1px solid #b9b9b9;background:linear-gradient(#dfe8f3 0 14%,#f4f6f9 14% 100%)}
.site p{font-size:11px;margin-top:7px;color:var(--ink);white-space:nowrap}
.office{left:699px;top:494px;width:333px;height:238px;background:linear-gradient(160deg,#bfae8f 0%,#8d7c63 45%,#6c6c6c 70%,#cfcfcf 100%)}
.data-box{left:699px;top:742px;width:338px;height:182px;border-radius:8px;border:1px solid #e3e6ea;
  background:linear-gradient(#e9eef4,#f7f8fa);box-shadow:0 1px 4px rgba(0,0,0,.12);padding:10px 8px}
.data-box h2{font-size:24px;font-weight:700;color:var(--heading);margin-bottom:5px}
.data-box p{font-size:10.6px;line-height:15.2px;color:var(--ink);letter-spacing:-.2px}

/* Footer */
.footer{left:0;top:932px;width:1200px;height:118px;background:linear-gradient(var(--footer),#6d6d6d)}
.fcol{top:14px;font-size:10.5px;line-height:13.5px;color:var(--footer-text)}
.fcol h4{font-size:10.5px;font-weight:700;color:#e2e2e2}
.copy{left:624px;top:14px;font-size:10.5px;font-weight:700;color:#e2e2e2}
.fbrand{left:626px;top:42px;display:flex;align-items:center;gap:6px}
.fbrand i{width:12px;height:12px;border-radius:50%;background:#c9ced6;display:block}
.fbrand span{font-size:15px;font-weight:700;color:#e6e9ee}
.social{left:763px;top:17px;display:flex;gap:11px}
.social i{width:21px;height:21px;border-radius:3px;display:block}
</style>
</head>
<body>

<header class="abs hero">
  <div class="abs utility">Home<span>|</span>Site Map</div>
  <div class="abs brand"><span class="brand-mark"></span><span class="brand-name">Pravelo</span></div>
  <nav class="abs nav">
    <a class="active" href="#" style="left:407px">Algemeen</a>
    <a href="#" style="left:521px">Producten</a>
    <a href="#" style="left:620px">Demo’s</a>
    <a href="#" style="left:718px">Media</a>
    <a href="#" style="left:815px">Referenties</a>
    <a href="#" style="left:913px">Peresoneel</a>
    <a href="#" style="left:1011px">Contact</a>
  </nav>
  <div class="abs hero-photo" role="img" aria-label="Group photo of five smiling business people standing together"></div>
  <h1 class="abs hero-title">Online Research Solutions</h1>
  <p class="abs hero-text">Aliquipit nis nis ad eriuscil utem vent prationsed el digna alit nonulluptat, venibh exerostie magnaeril ius.</p>
</header>

<section class="abs band"></section>
<div class="abs teaser" style="left:176px"><svg width="30" height="30" viewBox="0 0 30 30"><circle cx="15" cy="15" r="14" fill="#2a7fd6"/><text x="15" y="21" font-size="18" font-weight="700" fill="#fff" text-anchor="middle" font-family="Arimo,sans-serif">?</text></svg><p>Sub Headline<br>One <b>&gt;&gt;</b></p></div>
<div class="abs teaser" style="left:375px"><svg width="30" height="30" viewBox="0 0 30 30"><circle cx="15" cy="15" r="14" fill="#2a7fd6"/><text x="15" y="21" font-size="18" font-weight="700" fill="#fff" text-anchor="middle" font-family="Arimo,sans-serif">?</text></svg><p>Sub Headline<br>Two <b>&gt;&gt;</b></p></div>
<div class="abs teaser" style="left:566px"><svg width="30" height="30" viewBox="0 0 30 30"><circle cx="15" cy="15" r="14" fill="#2a7fd6"/><text x="15" y="21" font-size="18" font-weight="700" fill="#fff" text-anchor="middle" font-family="Arimo,sans-serif">?</text></svg><p>Sub Headline<br>Three <b>&gt;&gt;</b></p></div>
<div class="abs teaser" style="left:787px"><svg width="30" height="30" viewBox="0 0 30 30"><circle cx="15" cy="15" r="14" fill="#2a7fd6"/><text x="15" y="21" font-size="18" font-weight="700" fill="#fff" text-anchor="middle" font-family="Arimo,sans-serif">?</text></svg><p>Sub Headline<br>Four <b>&gt;&gt;</b></p></div>

<main>
  <h2 class="abs welcome">Welcome to Pravelo</h2>
  <p class="abs lead">Pravelo is gespecialiseerd in online gegevensverzameling en analyse en is werkzaam voor internationale opdrachtgevers.</p>
  <div class="abs body-copy">
    <p>Het bedrijf werd opgericht in 1997 en is gevestigd in Veldwater, een kleine havenplaats boven Amsterdam. Onze produkten zijn ontwikkeld op basis van Q, een krachtige en uitermate flexibele onderzoekstool voor het verzamelen &amp; verwerken van (online) researchgegevens. Q werd ontwikkeld dóór opinieonderzoekers vóór opinieonderzoekers.</p>
    <p>Ons team bestaat uit zowel opinieonderzoekers als programmeurs met vele jaren ervaring op het gebied van opinieonderzoek en met name met online toepassingen daarvoor.</p>
    <p>Deze bekende sites zijn ontwikkeld en worden beheerd door Pravelo BV:</p>
  </div>

  <div class="abs site" style="left:165px"><div class="shot" role="img" aria-label="Screenshot of the meetpunt panel website"></div><p>meetpunt.pravelo.nl</p></div>
  <div class="abs site" style="left:328px"><div class="shot" role="img" aria-label="Screenshot of the kijkkamer panel website"></div><p>kijkkamer.pravelo.nl</p></div>
  <div class="abs site" style="left:487px"><div class="shot" role="img" aria-label="Screenshot of the jongpeil panel website"></div><p>jongpeil.pravelo.nl</p></div>

  <div class="abs office" role="img" aria-label="Photo of the office with staff working at computers on a checkered floor"></div>
  <aside class="abs data-box">
    <h2>Data collection</h2>
    <p>Pravelo is uitgegroeid tot een volwaardig speler in de markt met een indrukwekkend(e) portfolio. Zo heeft Pravelo sinds haar oprichting wereldwijd meer dan 2.000.000 vragenlijsten afgenomen in diverse talen en voor diverse opdrachtgevers. Onze dienstverlening beperkt zich tot het verzamelen van data, Pravelo trekt geen conclusies maar stelt haar klanten middels ons online analyse product Q for Tables in staat zelf conclusies en/of rapportages te maken zodat beslissingen kunnen worden genomen op basis van eigen waarnemingen.</p>
  </aside>
</main>

<footer class="abs footer">
  <div class="abs fcol" style="left:210px"><h4>The Service</h4>About<br>Browse<br>Log In</div>
  <div class="abs fcol" style="left:334px"><h4>Support</h4>Contact Us<br>FAQ</div>
  <div class="abs fcol" style="left:451px"><h4>Legal</h4>Privacy Policy<br>Terms &amp; Conditions</div>
  <div class="abs copy">© 2010 Pravelo</div>
  <div class="abs fbrand"><i></i><span>Pravelo</span></div>
  <div class="abs social">
    <i style="background:#2b6fa8"></i><i style="background:#3b5a98"></i><i style="background:#3fb2e0"></i><i style="background:#e8782a"></i>
  </div>
</footer>

</body>
</html>
```